Premium modern eliquids labels 84.5 x 80 mm

I am looking for modern graphics for the labels of a new eliquid line that will have 4 different types of eliquids. It will have a tobacco one (brown colours maybe), a fruity one (bright colours maybe), a minty one (green colours maybe) and a creamy one (beige colours maybe).
I will need one of them to see how the design is, that design will have to be adapted to the other 3 colours of the label.
The brand logo is attached. I also attached a sample of what is mandatory to write on the label, you can change size, place and font of what is written, the only thing that cannot be reduced is the yellow parts. I attach the bottle that we will use.The size of the label is 84.5 x 80 mm (base x height).

Target Market(s)

vapers

Requirements
Must have
• My project must have one of the labels.

```html
<!DOCTYPE html>
<html lang="it">
<head>
<meta charset="utf-8">
<title>Etichetta eliquid – Menta</title>
<link rel="stylesheet" href="https://fonts.googleapis.com/css2?family=Barlow:wght@500;700;800&display=swap">
<style>
  :root {
    --green-deep: #021a06;
    --green-mid: #0a4a14;
    --green-glow: #17862a;
    --text-light: #ffffff;
    --label-yellow: #fcc62e;
    --label-ink: #111111;
    --brand-blue: #63b7e3;
  }
  html, body {
    margin: 0;
    padding: 0;
    width: 1200px;
    height: 1132px;
    overflow: hidden;
    background: var(--green-deep);
  }
  .label {
    position: relative;
    width: 1200px;
    height: 1132px;
    font-family: "Barlow", Arial, sans-serif;
    color: var(--text-light);
    overflow: hidden;
  }
  .label-background {
    position: absolute;
    inset: 0;
    background: radial-gradient(ellipse at 50% 50%, var(--green-glow) 0%, var(--green-mid) 45%, var(--green-deep) 100%);
  }
  .ingredients {
    position: absolute;
    left: 18px;
    top: 78px;
    width: 282px;
    text-align: center;
    font-weight: 800;
    font-size: 31px;
    line-height: 34px;
    text-transform: uppercase;
  }
  .batch-code {
    position: absolute;
    left: 68px;
    top: 552px;
    transform: translate(-50%, -50%) rotate(-90deg);
    white-space: nowrap;
    font-weight: 700;
    font-size: 20px;
  }
  .producer {
    position: absolute;
    left: 10px;
    top: 844px;
    width: 350px;
    text-align: center;
    font-weight: 500;
    font-size: 30px;
    line-height: 29.5px;
  }
  .brand-name {
    position: absolute;
    left: 593px;
    top: 524px;
    transform: translate(-50%, -50%);
    white-space: nowrap;
    font-weight: 800;
    font-size: 40px;
    letter-spacing: 1px;
    color: var(--brand-blue);
    text-transform: uppercase;
  }
  .usage {
    position: absolute;
    left: 908px;
    top: 74px;
    width: 250px;
    text-align: center;
    font-size: 29px;
    line-height: 33px;
    font-weight: 500;
  }
  .usage-title {
    font-weight: 800;
    text-transform: uppercase;
  }
  .disposal {
    position: absolute;
    left: 908px;
    top: 0;
    width: 250px;
    text-align: center;
  }
  .disposal-tag {
    position: absolute;
    left: 50%;
    transform: translateX(-50%);
    background: var(--label-yellow);
    color: var(--label-ink);
    font-weight: 800;
    text-align: center;
    text-transform: uppercase;
    display: flex;
    align-items: center;
    justify-content: center;
  }
  .tag-collection {
    width: 172px;
    height: 71px;
    font-size: 27px;
    line-height: 29px;
  }
  .tag-code {
    width: 130px;
    height: 53px;
    font-size: 38px;
  }
  .disposal-part {
    position: absolute;
    left: 0;
    right: 0;
    font-size: 29px;
    font-weight: 500;
    text-transform: uppercase;
  }
  .icon-recycle {
    position: absolute;
    left: 943px;
    top: 949px;
    width: 84px;
    height: 80px;
  }
  .icon-bin {
    position: absolute;
    left: 1045px;
    top: 917px;
    width: 78px;
    height: 114px;
  }
  .net-volume {
    position: absolute;
    left: 908px;
    top: 1054px;
    width: 250px;
    text-align: center;
    font-weight: 700;
    font-size: 30px;
  }
</style>
</head>
<body>
<main class="label">
  <div class="label-background" role="img" aria-label="Motivo decorativo ornamentale verde con bagliore centrale"></div>

  <div class="ingredients">Ingredienti:<br>Glicole<br>propilenico<br>sostanze<br>aromatizzanti</div>

  <div class="batch-code">L.SH20 - 001-PES-D.PROD-22-04-2022 D.SC.21-04-2024</div>

  <div class="brand-name">Verdant Drops</div>

  <div class="producer">PRODOTTO<br>E CONFEZIONATO<br>DA Verdant srl<br>Via dei Tigli 18<br>20121 Milano<br>P.i.12345678901<br>Tel. +39 02 5550199<br>info@verdant.it</div>

  <div class="usage">
    <div class="usage-title">Istruzioni<br>d’uso:</div>
    Agitare bene<br>prima<br>dell’utilizzo.<br>Diluire nelle<br>percentuali<br>consigliate<br>sul nostro<br>sito.<br>Conservare in<br>luogo fresco e<br>asciutto
  </div>

  <div class="disposal">
    <div class="disposal-tag tag-collection" style="top:522px">Raccolta<br>plastica</div>
    <div class="disposal-part" style="top:607px">Etichetta</div>
    <div class="disposal-tag tag-code" style="top:658px">PAP 5</div>
    <div class="disposal-tag tag-collection" style="top:721px">Raccolta<br>plastica</div>
    <div class="disposal-part" style="top:796px">Flacone</div>
    <div class="disposal-tag tag-code" style="top:845px">PET 1</div>
  </div>

  <svg class="icon-recycle" viewBox="0 0 84 80" aria-hidden="true">
    <g fill="none" stroke="#ffffff" stroke-width="6" stroke-linejoin="round">
      <path d="M28 30 L38 13 Q42 7 46 13 L52 23"/>
      <path d="M62 42 L72 60 Q75 67 67 67 L56 67"/>
      <path d="M36 67 L16 67 Q9 67 12 60 L18 49"/>
    </g>
    <g fill="#ffffff">
      <polygon points="44,26 62,18 60,36"/>
      <polygon points="58,57 58,77 44,67"/>
      <polygon points="8,44 26,42 22,58"/>
    </g>
  </svg>

  <svg class="icon-bin" viewBox="0 0 78 114" aria-hidden="true">
    <g fill="#ffffff">
      <circle cx="50" cy="10" r="8"/>
      <path d="M40 22 H60 V66 H56 V112 H50 V70 H48 V112 H42 V66 H40 V46 L28 58 L24 54 L40 36 Z"/>
      <path d="M2 66 H34 L30 112 H6 Z"/>
    </g>
    <g stroke="#1b5e22" stroke-width="3">
      <line x1="12" y1="74" x2="14" y2="104"/>
      <line x1="24" y1="74" x2="22" y2="104"/>
    </g>
  </svg>

  <div class="net-volume">20 ML NET</div>
</main>
</body>
</html>
```